Manufacturing Company Business card

K & T is a leading supplier of complex machine parts, assemblies and sub assemblies to the aerospace industry.
we would like to create a new feel for our manufacturing company business card design.
We are into lean manufacturing, bold design, metal, use current logo, use "this is your life" logo for entire back of card. updated look for 2015, text, bardcode, etc

our primary end use is flight control components used on about all commercial and business jets in use as well as military aircraft and civil aviation.

Reason: Need more time to review with internal team at KTmfg:)

Target Market(s)

aerospace, manufacturing

Industry/Entity Type

Aero

Contact Information for Business Card

New, industrial, trendy, use current logo, we like text, vmail is lame :( cell ph is ok - what is a fax???

Font styles to use
Serif
Sans Serif

Requirements
Must have
• incorporate our current logo, one option is an Industrial look, metal etc. we can also try to incorporate the feel of the back of the card onto the front but not so busy.
• Back of card full size "this is your life"
• front side, barcode, cell, - our motto "solutions in manufacturing" tm
Nice to have
• Professional look
• up to date
• appeals to broad audience
Should not have
• too much content - pictures of planes

```html
<!DOCTYPE html>
<html lang="en">
<head>
<meta charset="utf-8">
<title>K &amp; T Manufacturing – Business Card</title>
<link rel="stylesheet" href="https://fonts.googleapis.com/css2?family=Lato:wght@400;700&display=swap">
<style>
  :root {
    --backdrop: #3a322e;
    --card: #1c1c1c;
    --card-edge: #242424;
    --green: #14a550;
    --white: #ffffff;
    --light: #d2d2d2;
    --muted: #7a7a7a;
    --faint: #262626;
  }
  * { margin: 0; padding: 0; box-sizing: border-box; }
  html, body {
    width: 1200px; height: 844px; overflow: hidden;
    background: var(--backdrop);
    font-family: "Lato", Arial, sans-serif;
  }
  .canvas {
    position: relative; width: 1200px; height: 844px;
    display: flex; align-items: center; justify-content: center; gap: 60px;
  }
  .card {
    position: relative; width: 525px; height: 300px;
    background: linear-gradient(135deg, var(--card-edge), var(--card));
    overflow: hidden;
    box-shadow: 0 12px 30px rgba(0,0,0,.45);
  }
  /* Front */
  .band { position: absolute; left: 0; right: 0; height: 16px; background: var(--green); }
  .band--top { top: 0; }
  .band--bottom { bottom: 0; }
  .watermark-ring {
    position: absolute; left: 150px; top: 40px; width: 220px; height: 220px;
    border: 4px solid var(--faint); border-radius: 50%;
  }
  .identity { position: absolute; left: 220px; top: 48px; }
  .identity__name {
    color: var(--white); font-size: 19px; font-weight: 400; letter-spacing: .5px;
    padding-bottom: 4px; border-bottom: 2px solid var(--green);
  }
  .identity__role { color: var(--muted); font-size: 14px; margin-top: 4px; }
  .contact {
    position: absolute; right: 70px; top: 126px; text-align: right;
    color: var(--light); font-size: 14px; line-height: 20px;
  }
  .address {
    position: absolute; left: 32px; bottom: 40px;
    color: var(--light); font-size: 14px;
  }
  /* Back */
  .tab {
    position: absolute; width: 20px; height: 46px;
    background: linear-gradient(90deg, var(--green) 70%, var(--white) 70%);
  }
  .tab--right { right: 0; top: 18px; }
  .tab--left { left: 0; bottom: 30px; transform: scaleX(-1); }
  .brand {
    position: absolute; inset: 0;
    display: flex; align-items: center; justify-content: center; gap: 14px;
  }
  .brand__dot { width: 22px; height: 22px; border-radius: 50%; background: var(--green); }
  .brand__name {
    color: var(--white); font-size: 28px; font-weight: 700; letter-spacing: 1.5px;
  }
</style>
</head>
<body>
<main class="canvas">
  <section class="card card--front" aria-label="Card front">
    <div class="band band--top"></div>
    <div class="watermark-ring"></div>
    <div class="identity">
      <p class="identity__name">DANIEL HARPER</p>
      <p class="identity__role">Managing Director</p>
    </div>
    <div class="contact">
      <p>044-555-0142</p>
      <p>123-555-0187</p>
      <p>info@ktmfg.com</p>
      <p>www.ktmfg.com</p>
    </div>
    <p class="address">1840 Hangar Way | Ridgeview, AB | 654321</p>
    <div class="band band--bottom"></div>
  </section>

  <section class="card card--back" aria-label="Card back">
    <div class="tab tab--right"></div>
    <div class="brand">
      <span class="brand__dot"></span>
      <span class="brand__name">K &amp; T MANUFACTURING</span>
    </div>
    <div class="tab tab--left"></div>
  </section>
</main>
</body>
</html>
```